Nutrition Consulting Business needs a Postcard

I am a nutritionist and I need a brochure that highlights my consulting company called, GreenLeaf OakPath. Nutrition counselling helps the individual understand why we make certain health choices and help achieve meaningful resolutions to these difficult roadblocks. It is the practice of incorporating diverse nutritional and health philosophies to identify and achieve goals that lead to improved health and well-being. Nutrition counselling facilitates personal ownership in ones life choices, and provides the individual with the knowledge and the resources to make decisions that will be vital to their health and well-being. The important caveat of nutrition counselling is to gradually modify ones choices to ensure that changes last the their whole life. I want something that is professional, clean and makes people want to kickstart their wellness journey.
www.greenleafoakpath.example
Updates

I have updated the project profile (more detail) and changed to a guaranteed funds project. happy designing!

Target Market(s)

open minded adults and families wanting to make changes to better their health, those with gastrointestinal problems

Industry/Entity Type

Nutrition

Requirements
Must have
• The brochure must have my logo but I am open to font etc. I would liek to stick with 'earthy' colours, focusing on greens, like in my logo with eggplant as an accent colour.

Email: marla@greenleafoakpath.example
FB: https://www.facebook.com/greenleafoakpath
T: @greenleafoakpath

I am not sure what would be the best way to display this information. Maybe you have some ideas?

I would like to have my name and credentials stated somewhere. It is my PhD that sets be apart from others in the industry.
Marla Quenby
PhD Clinical Nutrition
Certified Health Coach

My main tag line is: "Leaf green, path oak." Maybe that could be the focus on the front side. With the 'big changes' quote on the backside somewhere.

Also, I think it would be valuable to have a brief list of services (what I do):
Individual Consultations
Workshops
Corporate Seminars
Meal Planning
Fresh Start Reset

Feel free to use any content from my website.
Nice to have
• I would prefer a two sided card type brochure. It would be nice if the design could easily fit to a 4X6 index/recipe card format also.

```html
<!DOCTYPE html>
<html lang="en">
<head>
<meta charset="utf-8">
<title>GreenLeaf OakPath – Nutrition Postcard</title>
<link rel="stylesheet" href="https://fonts.googleapis.com/css2?family=Great+Vibes&family=Questrial&display=swap">
<style>
  :root {
    --eggplant: #7b4a7a;
    --olive: #a3ab2c;
    --olive-dark: #8f9a24;
    --ink: #3d3d3d;
    --paper: #ffffff;
    --backdrop: #ffffff;
    --edge: #d9d9d9;
    --lentil: #8a5a2e;
    --berry: #3b4663;
    --nut: #9a6434;
    --grain: #c5a77a;
    --leaf: #4f6b2a;
  }
  * { box-sizing: border-box; margin: 0; padding: 0; }
  html, body {
    width: 1200px; height: 900px; overflow: hidden;
    background: var(--backdrop);
    font-family: "Questrial", "Century Gothic", sans-serif;
  }
  .canvas { position: relative; width: 1200px; height: 900px; }

  .card {
    position: absolute; width: 500px; height: 750px;
    background: var(--paper);
    border: 1px solid var(--edge);
    box-shadow: 3px 4px 6px rgba(0,0,0,.18);
    overflow: hidden;
  }
  .card--front { left: 68px; top: 40px; }
  .card--back  { left: 630px; top: 110px; }

  /* Front */
  .owner-name {
    position: absolute; left: 30px; top: 42px; width: 440px;
    font-family: "Great Vibes", cursive; font-size: 80px; font-weight: 400; line-height: 1;
    color: #111; text-align: center; white-space: nowrap;
  }
  .owner-degree {
    position: absolute; left: 408px; top: 108px;
    font-size: 10px; color: #111;
  }
  .credentials {
    position: absolute; left: 112px; top: 126px;
    color: var(--eggplant); font-size: 19px; line-height: 23px; text-align: center;
  }
  .brand-mark {
    position: absolute; left: 0; top: 250px; width: 500px; text-align: center;
  }
  .brand-mark__dot {
    display: block; width: 90px; height: 90px; margin: 0 auto 18px;
    border-radius: 50%; background: var(--olive);
  }
  .brand-mark__name {
    font-size: 38px; color: var(--eggplant); letter-spacing: -.5px;
  }
  .front-pitch {
    position: absolute; left: 55px; top: 488px; width: 390px;
    color: var(--olive); font-size: 15px; line-height: 21px; text-align: center;
  }
  .food-strip {
    position: absolute; left: 0; bottom: 0; width: 500px; height: 133px;
    display: flex;
  }
  .food-strip__tile { flex: 1; }
  .tile--lentils { background: linear-gradient(135deg, #6c5a3a, var(--lentil)); }
  .tile--berries { background: linear-gradient(135deg, #2d3550, var(--berry)); }
  .tile--nuts    { background: linear-gradient(135deg, #7a4a26, var(--nut)); }
  .tile--grains  { background: linear-gradient(135deg, #8a6a48, var(--grain)); }
  .tile--greens  { background: linear-gradient(135deg, #3a4f1e, var(--leaf)); }

  /* Back */
  .quote {
    position: absolute; left: 32px; top: 38px; width: 440px;
    color: var(--eggplant); font-size: 27px; line-height: 29px; font-style: italic;
  }
  .section-bar {
    position: absolute; left: 32px; width: 418px; height: 23px;
    padding-left: 12px; line-height: 23px;
    color: #fff; font-size: 15px; font-weight: bold;
    background: linear-gradient(90deg, var(--olive-dark) 0%, var(--olive) 55%, rgba(163,171,44,0) 100%);
  }
  .section-bar--about    { top: 150px; }
  .section-bar--services { top: 395px; }
  .section-bar--contact  { top: 515px; }
  .about-text {
    position: absolute; left: 17px; top: 181px; width: 390px;
    color: var(--ink); font-size: 13.8px; line-height: 20.8px;
  }
  .service-list {
    position: absolute; left: 44px; top: 426px; width: 420px;
    list-style: none; columns: 2; column-gap: 0;
    color: var(--ink); font-size: 15px; line-height: 20.8px;
  }
  .service-list li::before { content: "•"; margin-right: 8px; font-size: 11px; vertical-align: 2px; }
  .coach-photo {
    position: absolute; left: 44px; top: 550px; width: 94px; height: 96px;
    background: linear-gradient(160deg, #8d8a80, #5e5a52);
  }
  .contact-list {
    position: absolute; left: 149px; top: 545px;
    list-style: none; color: var(--ink); font-size: 15px; line-height: 21px;
  }
  .contact-list li { display: flex; }
  .contact-list .label { width: 18px; }
  .contact-list .value { width: 260px; overflow-wrap: anywhere; }
  .brand-sign {
    position: absolute; right: 30px; top: 652px; text-align: right;
  }
  .brand-sign__dot {
    display: block; width: 44px; height: 44px; margin: 0 60px 10px auto;
    border-radius: 50%; background: var(--olive);
  }
  .brand-sign__name { font-size: 19px; color: var(--eggplant); }
</style>
</head>
<body>
<main class="canvas">

  <section class="card card--front">
    <h1 class="owner-name">Marla Quenby</h1>
    <span class="owner-degree">PhD.</span>
    <p class="credentials">Clinical Nutrition<br>Certified Health Coach</p>

    <div class="brand-mark">
      <span class="brand-mark__dot"></span>
      <span class="brand-mark__name">GreenLeaf OakPath</span>
    </div>

    <p class="front-pitch">Taking control of your health starts with understanding your body. I give resources and take the guesswork out of planning for your health. Arm yourself with knowledge and let me set you on an attainable program that’s right for you</p>

    <div class="food-strip">
      <div class="food-strip__tile tile--lentils" role="img" aria-label="Wooden spoon of mixed lentils and beans"></div>
      <div class="food-strip__tile tile--berries" role="img" aria-label="Wooden spoon of blueberries"></div>
      <div class="food-strip__tile tile--nuts" role="img" aria-label="Wooden spoon of mixed nuts"></div>
      <div class="food-strip__tile tile--grains" role="img" aria-label="Wooden spoon of quinoa"></div>
      <div class="food-strip__tile tile--greens" role="img" aria-label="Wooden spoon of spinach leaves"></div>
    </div>
  </section>

  <section class="card card--back">
    <blockquote class="quote">“Big commitments to small changes outlast small commitments to big changes.”</blockquote>

    <h2 class="section-bar section-bar--about">What is nutrition counselling?</h2>
    <p class="about-text">It is the practice of incorporating diverse nutritional and health philosophies to identify and achieve goals that lead to improved health and well-being. Nutrition counselling facilitates personal ownership in your life choices, and provides you with the knowledge and the resources to make decisions that will be <em>vital</em> to your health and well-being. The important caveat of nutrition counselling is to gradually modify your choices to ensure that changes last your <em>whole</em> life.</p>

    <h2 class="section-bar section-bar--services">Services</h2>
    <ul class="service-list">
      <li>Individual Consultations</li>
      <li>Workshops</li>
      <li>Corporate Seminars</li>
      <li>Grocery Store Tour</li>
      <li>Meal Planning</li>
      <li>Fresh Start Reset</li>
    </ul>

    <h2 class="section-bar section-bar--contact">Contact Marla today</h2>
    <div class="coach-photo" role="img" aria-label="Portrait photo of the nutritionist"></div>
    <ul class="contact-list">
      <li><span class="label">w:</span><span class="value">www.greenleafoakpath.example</span></li>
      <li><span class="label">e:</span><span class="value">marla@greenleafoakpath.example</span></li>
      <li><span class="label">f:</span><span class="value">https://social.example/<br>greenleafoakpath</span></li>
      <li><span class="label">t:</span><span class="value">@greenleafoakpath</span></li>
    </ul>

    <div class="brand-sign">
      <span class="brand-sign__dot"></span>
      <span class="brand-sign__name">GreenLeaf OakPath</span>
    </div>
  </section>

</main>
</body>
</html>
```